Business card for a gourmet fruit and vegetable retail store

Please design a business card for our boutique gourmet fruit and vegetable food store using attached logo design, with the colour options of white, black and lime green. We would like it to be unique and classic, with a large image of the logo on the back of the business card, and the business card details plus a design on the front.

Target Market(s)

High income earners in an affluent Melbourne suburb who value high quality products and done mind paying for it

Industry/Entity Type

Retail

Contact Information for Business Card

Business name: Haddleby's Fine Food Merchant
Address: 27 Quillmont Rd, Tarnvale VIC 3188
Name: TBC
Position Title: Director
Phone Number: TBC
Mobile: TBC

Business name is: Haddleby's Fine Food Merchant. Please allow space for us to fill in the business address, contact number, person's name, position Title and mobile number.

Colors
acd036

Requirements
Must have
• The logo must have our business logo on the back, and our business details and contact details on the front. It must include the colours of white, black and lime green
Nice to have
• It can have different background colours on the front and on the back.
Should not have
• It should not have any other colours aside from white, black and lime green

```html
<!DOCTYPE html>
<html lang="en">
<head>
<meta charset="utf-8">
<title>Haddleby's Fine Food Merchant – Business Card</title>
<link href="https://fonts.googleapis.com/css2?family=Roboto+Slab:wght@400;700&display=swap" rel="stylesheet">
<style>
  :root {
    --lime: #acd036;
    --black: #0d0d0d;
    --ink: #111111;
    --white: #f4f4f4;
    --stage: #1c1c1c;
    --rule: #444444;
  }
  * { box-sizing: border-box; margin: 0; padding: 0; }
  html, body {
    width: 1200px; height: 900px; overflow: hidden;
    background: var(--stage);
    font-family: "Roboto Slab", Georgia, serif;
  }
  .canvas {
    width: 1200px; height: 900px;
    display: flex; align-items: center; justify-content: center; gap: 40px;
  }
  .card {
    position: relative;
    width: 540px; height: 310px;
    overflow: hidden;
    box-shadow: 0 18px 40px rgba(0,0,0,.55);
  }
  .card-front { background: var(--white); }
  .card-back { background: var(--black); }
  .front-art { position: absolute; inset: 0; }

  .business-name {
    position: absolute;
    display: flex; align-items: center; gap: 8px;
    font-weight: 700; white-space: nowrap;
  }
  .business-name .mark { flex: none; border-radius: 50%; }
  .front-name { left: 268px; top: 262px; font-size: 13px; color: var(--ink); }
  .front-name .mark { width: 10px; height: 10px; background: var(--lime); }
  .back-name {
    left: 0; right: 0; top: 50%; transform: translateY(-50%);
    justify-content: center; font-size: 24px; color: var(--lime);
  }
  .back-name .mark { width: 16px; height: 16px; background: var(--lime); }

  .contact { position: absolute; left: 36px; color: var(--ink); font-weight: 700; }
  .person { top: 42px; }
  .person .name { font-size: 17px; letter-spacing: .5px; text-transform: uppercase; }
  .person .role { font-size: 11px; font-weight: 400; color: var(--lime); text-transform: uppercase; margin-top: 3px; }
  .divider { position: absolute; left: 38px; width: 2px; height: 20px; background: var(--rule); transform: skewX(-25deg); }
  .divider-one { top: 100px; }
  .divider-two { top: 188px; }
  .address { top: 132px; font-size: 12.5px; line-height: 1.45; text-transform: uppercase; }
  .phones { top: 218px; font-size: 13px; line-height: 1.7; }
  .phone-line { display: flex; align-items: center; gap: 8px; }
  .phone-icon { width: 14px; height: 14px; }
</style>
</head>
<body>
<main class="canvas">

  <section class="card card-front" aria-label="Business card front">
    <svg class="front-art" viewBox="0 0 540 310" width="540" height="310" aria-hidden="true">
      <path fill="var(--black)" d="M170,0 H540 V255 C460,235 390,170 330,95 C290,45 240,10 170,0Z"/>
      <path fill="var(--white)" d="M195,0 H540 V245 C465,225 395,160 340,90 C300,40 255,10 195,0Z"/>
      <path fill="var(--lime)" d="M215,0 H540 V232 C470,212 405,150 352,85 C315,40 272,12 215,0Z"/>
      <path fill="var(--black)" d="M245,0 H540 V215 C475,195 415,138 365,78 C330,38 290,12 245,0Z"/>
      <path fill="var(--black)" d="M540,262 V310 H455 C485,292 512,278 540,262Z"/>
      <polygon fill="var(--lime)" points="0,297 250,297 263,310 0,310"/>
    </svg>

    <p class="business-name front-name"><span class="mark"></span>Haddleby's Fine Food Merchant</p>

    <div class="contact person">
      <p class="name">Marcus Thorne</p>
      <p class="role">Director</p>
    </div>
    <span class="divider divider-one"></span>
    <p class="contact address">27 Quillmont Rd<br>Tarnvale VIC 3188</p>
    <span class="divider divider-two"></span>
    <div class="contact phones">
      <p class="phone-line">
        <svg class="phone-icon" viewBox="0 0 14 14" aria-hidden="true"><circle cx="7" cy="7" r="7" fill="var(--lime)"/><rect x="4" y="4.5" width="6" height="5" rx="1" fill="var(--ink)"/></svg>
        0234-5510-8872
      </p>
      <p class="phone-line">
        <svg class="phone-icon" viewBox="0 0 14 14" aria-hidden="true"><circle cx="7" cy="7" r="7" fill="var(--lime)"/><rect x="4.5" y="3" width="5" height="8" rx="1" fill="var(--ink)"/></svg>
        0234-5510-8872
      </p>
    </div>
  </section>

  <section class="card card-back" aria-label="Business card back">
    <p class="business-name back-name"><span class="mark"></span>Haddleby's Fine Food Merchant</p>
  </section>

</main>
</body>
</html>
```